Website for Brisbeck Current Glide

Require a website for a river float in the City of Edmonton. Located on North Saskatchewan River. Will need to be a coded website with incorporated booking system through Fare Harbor software.

Pages include
Home
Pricing
About
FAQ
Contact

Brisbeck Current Glide is an activity based business that will have customers floating down the North Saskatchewan river in Edmonton AB. The site will have all information needed and a full reservation system. The project was launched to provide people in the Edmonton area a favorite summer activity.

Here are similar websites to reference what our business will be doing and what we are looking for.

mellowbendcanoehire.example
pinegulchloopers.example

Target Market(s)

Families, Groups, Individuals, Anyone who wants to explore the river

Industry/Entity Type

Activities based business/ Outdoor recreational/ River Float

Coding

Coded - Design and coding required

Number of Pages Required

5+ page

Colors
0054AA
0677BA
7BADD7
CADEEF
E8F1F8
F0912C
F2A743
F7CA91
FBE8D2
FDF5EE

```html
<!DOCTYPE html>
<html lang="en">
<head>
<meta charset="utf-8">
<title>Brisbeck Current Glide – Home</title>
<link href="https://fonts.googleapis.com/css2?family=Montserrat:wght@700;800;900&family=Mulish:wght@400;600&display=swap" rel="stylesheet">
<style>
:root{
  --navy:#0a2f66;
  --blue-deep:#0054AA;
  --blue:#0677BA;
  --blue-mid:#7BADD7;
  --blue-light:#CADEEF;
  --blue-pale:#E8F1F8;
  --sky:#4fc3e3;
  --orange:#F0912C;
  --orange-soft:#F2A743;
  --peach:#F7CA91;
  --cream:#FBE8D2;
  --cream-pale:#FDF5EE;
  --ink:#333;
  --white:#fff;
}
*{box-sizing:border-box;margin:0;padding:0}
html,body{width:1200px;height:2252px;overflow:hidden}
body{position:relative;background:var(--white);font-family:"Mulish",sans-serif;color:var(--ink)}
.abs{position:absolute}
.heading{font-family:"Montserrat",sans-serif;font-weight:900;color:var(--navy);text-transform:uppercase;line-height:1.3}
.btn{position:absolute;display:flex;align-items:center;justify-content:center;background:var(--orange);color:var(--white);
  font-family:"Montserrat",sans-serif;font-weight:800;font-size:12px;letter-spacing:.3px;text-transform:uppercase;
  border-radius:30px;box-shadow:0 0 0 3px var(--white),0 0 0 5px var(--orange)}
/* header */
.site-header{position:absolute;left:0;top:0;width:1200px;height:102px;background:var(--white);z-index:3}
.brand{position:absolute;left:150px;top:0;width:160px;height:148px;border-radius:0 0 80px 80px;background:var(--white);z-index:4;
  display:flex;flex-direction:column;align-items:center;justify-content:center;gap:8px}
.brand-dot{width:52px;height:52px;border-radius:50%;background:var(--sky)}
.brand-name{font-family:"Montserrat",sans-serif;font-weight:800;font-size:15px;color:var(--navy);text-align:center;line-height:1.15;text-transform:uppercase}
.main-nav a{position:absolute;top:43px;font-family:"Montserrat",sans-serif;font-weight:800;font-size:13px;color:var(--navy);text-decoration:none}
.main-nav a.active{color:var(--orange)}
/* hero */
.hero{position:absolute;left:0;top:102px;width:1200px;height:560px}
.hero-kicker{left:661px;top:138px;font-size:23px;color:var(--white)}
.hero-title{left:661px;top:168px;font-size:37px;color:var(--white);line-height:1.22}
.hero-sub{left:662px;top:262px;font-size:23px;color:var(--white)}
/* features */
.feature-title{font-size:33px}
.feature-text{font-size:16px;line-height:28px;color:#333}
/* footer */
.site-footer{position:absolute;left:0;top:1680px;width:1200px;height:572px;
  background:linear-gradient(180deg,var(--white) 0%,var(--blue-pale) 10%,var(--blue-mid) 26%,#2f8fd6 30%,#2f86d9 55%,var(--blue-deep) 100%)}
.foot-head{position:absolute;top:268px;font-family:"Montserrat",sans-serif;font-weight:800;font-size:16px;color:var(--peach);text-transform:uppercase}
.quick-links{position:absolute;left:164px;top:308px;list-style:none}
.quick-links li{font-size:14px;color:var(--white);height:28.6px}
.quick-links li::before{content:"»";font-size:11px;margin-right:10px}
.contact-item{position:absolute;left:318px;display:flex;gap:14px;color:var(--white);font-size:13px;line-height:20px}
.contact-icon{width:30px;height:30px;border-radius:50%;background:var(--orange);flex:none;display:flex;align-items:center;justify-content:center;margin-top:2px}
.contact-item b{font-family:"Montserrat",sans-serif;font-weight:700;color:var(--cream);font-size:13px;text-transform:uppercase;display:block}
.newsletter-note{position:absolute;left:585px;top:308px;width:230px;font-size:12px;color:var(--white);line-height:16px}
.email-field{position:absolute;left:585px;top:345px;width:229px;height:41px;border-radius:21px;background:var(--white);
  display:flex;align-items:center;padding-left:20px;gap:10px;font-size:14px;color:#333}
.footer-brand{position:absolute;left:850px;top:290px;width:190px;display:flex;flex-direction:column;align-items:center;gap:14px}
.footer-brand .brand-dot{width:120px;height:120px;background:var(--blue-pale)}
.footer-brand .brand-name{color:var(--white);font-size:20px}
.copyright-bar{position:absolute;left:0;bottom:0;width:1200px;height:44px;background:#0a4da0;color:var(--white);font-size:14px}
.copyright-bar p{position:absolute;left:164px;top:13px}
.social{position:absolute;top:8px;width:31px;height:31px;border-radius:50%;background:var(--white)}
</style>
</head>
<body>

<header class="site-header">
  <div class="brand"><span class="brand-dot"></span><span class="brand-name">Brisbeck<br>Current Glide</span></div>
  <nav class="main-nav">
    <a class="active" style="left:535px">Home</a>
    <a style="left:617px">Pricing</a>
    <a style="left:717px">About Us</a>
    <a style="left:832px">FAQs</a>
  </nav>
  <div class="btn" style="left:910px;top:30px;width:128px;height:44px">Contact Us</div>
</header>

<section class="hero">
  <svg class="abs" width="1200" height="560" viewBox="0 0 1200 560" style="left:0;top:0">
    <defs>
      <linearGradient id="heroPhoto" x1="0" y1="0" x2="0" y2="1">
        <stop offset="0" stop-color="#5f8a55"/>
        <stop offset=".2" stop-color="#3f6f8c"/>
        <stop offset=".55" stop-color="#2f5f96"/>
        <stop offset="1" stop-color="#1d4a84"/>
      </linearGradient>
    </defs>
    <rect width="1200" height="560" fill="var(--white)"/>
    <path d="M0 0H1200V455C1100 500 900 540 600 520C350 500 150 460 0 475Z" fill="url(#heroPhoto)" role="img" aria-label="Photo: two children riding a yellow inflatable tube across a river"/>
    <path d="M0 475C150 440 330 440 500 470C550 480 600 495 660 508C500 560 250 575 0 485Z" fill="var(--cream)"/>
    <path d="M1040 490C1100 480 1160 460 1200 455V500C1150 500 1090 495 1040 490Z" fill="var(--cream)"/>
  </svg>
  <p class="abs hero-kicker">Brisbeck Current Glide</p>
  <h1 class="abs heading hero-title">Float the North<br>Saskatchewan</h1>
  <p class="abs hero-sub">Through Downtown Edmonton</p>
  <div class="btn" style="left:663px;top:312px;width:129px;height:44px">Book Now</div>
</section>

<section class="feature">
  <svg class="abs" width="410" height="400" viewBox="0 0 410 400" style="left:158px;top:780px">
    <defs><linearGradient id="f1" x1="0" y1="0" x2="1" y2="1"><stop offset="0" stop-color="#b9cfd6"/><stop offset=".5" stop-color="#c9a53a"/><stop offset="1" stop-color="#3c6e4a"/></linearGradient></defs>
    <path d="M150 25C220 -10 330 0 375 90C410 170 395 280 320 345C250 400 140 405 70 360C10 320 -5 230 20 160C40 100 90 55 150 25Z" fill="var(--sky)"/>
    <path d="M140 35C210 5 310 20 355 100C390 170 380 270 305 335C240 385 140 390 75 350C20 315 2 230 25 165C45 105 90 60 140 35Z" fill="url(#f1)" role="img" aria-label="Photo: staff member fitting a life jacket on a guest"/>
  </svg>
  <h2 class="abs heading feature-title" style="left:628px;top:843px">Shuttle Service and<br>Gear Include</h2>
  <p class="abs feature-text" style="left:631px;top:943px;width:420px">We provide everything you need including round trip shuttle service, float tube, lifejacket, paddle, and more. Fun for everyone!</p>
  <div class="btn" style="left:630px;top:1059px;width:129px;height:44px">Learn More</div>
</section>

<section class="feature">
  <h2 class="abs heading feature-title" style="left:160px;top:1279px">Floating 7 and<br>Days a Week</h2>
  <p class="abs feature-text" style="left:163px;top:1378px;width:410px">Our priority is to make sure everyone has a safe and fun time on the river. Safety demonstrations are provided and staff are available to assist in any way.Whether you are a family with children, larger group or just want a relaxing way to explore the river, this is a must try activity.</p>
  <div class="btn" style="left:163px;top:1576px;width:129px;height:44px">Learn More</div>
  <svg class="abs" width="410" height="400" viewBox="0 0 410 400" style="left:637px;top:1231px">
    <defs><linearGradient id="f2" x1="0" y1="0" x2="1" y2="1"><stop offset="0" stop-color="#6d9bc0"/><stop offset=".5" stop-color="#3f79ad"/><stop offset="1" stop-color="#2d5f8d"/></linearGradient></defs>
    <path d="M150 25C220 -10 330 0 375 90C410 170 395 280 320 345C250 400 140 405 70 360C10 320 -5 230 20 160C40 100 90 55 150 25Z" fill="var(--sky)"/>
    <path d="M140 35C210 5 310 20 355 100C390 170 380 270 305 335C240 385 140 390 75 350C20 315 2 230 25 165C45 105 90 60 140 35Z" fill="url(#f2)" role="img" aria-label="Photo: group of people relaxing on float tubes on the river"/>
  </svg>
</section>

<footer class="site-footer">
  <svg class="abs" width="1200" height="40" viewBox="0 0 1200 40" style="left:0;top:150px">
    <path d="M0 22C80 12 160 20 240 16S420 6 520 18S720 26 820 14S1040 8 1200 20" fill="none" stroke="var(--blue-deep)" stroke-width="3" opacity=".6"/>
  </svg>

  <h3 class="foot-head" style="left:164px">Quick Links</h3>
  <ul class="quick-links">
    <li>Home</li><li>Pricing</li><li>About Us</li><li>FAQs</li><li>Contact Us</li>
  </ul>

  <h3 class="foot-head" style="left:318px">Contact Details</h3>
  <div class="contact-item" style="top:308px">
    <span class="contact-icon"><svg width="12" height="16" viewBox="0 0 12 16"><path d="M6 0C2.7 0 0 2.6 0 5.9 0 10.3 6 16 6 16S12 10.3 12 5.9C12 2.6 9.3 0 6 0Zm0 8.2A2.3 2.3 0 1 1 6 3.6a2.3 2.3 0 0 1 0 4.6Z" fill="#fff"/></svg></span>
    <div><b>Brisbeck Current Glide</b>4410 Harrow Lane NW,<br>Edmonton, AB</div>
  </div>
  <div class="contact-item" style="top:386px">
    <span class="contact-icon"><svg width="14" height="14" viewBox="0 0 14 14"><path d="M3 0 5 3.5 3.6 5C4.5 7 6.9 9.5 9 10.4l1.5-1.4L14 11l-1.2 2.6C6.5 14 0 7.5.4 1.2Z" fill="#fff"/></svg></span>
    <div><b>Phone</b>555 014 2290</div>
  </div>
  <div class="contact-item" style="top:445px">
    <span class="contact-icon"><svg width="15" height="11" viewBox="0 0 15 11"><rect x=".5" y=".5" width="14" height="10" rx="1" fill="none" stroke="#fff"/><path d="M.5 .5 7.5 6l7-5.5M.5 10.5 5.5 5.5m9 5-5-5" fill="none" stroke="#fff"/></svg></span>
    <div><b>Email</b>info@brisbeckglide.example</div>
  </div>

  <h3 class="foot-head" style="left:585px">Newsletter Signup</h3>
  <p class="newsletter-note">Lorem ipsum dolor sit amet, consecuer adipiscing elit, sed diam !</p>
  <div class="email-field"><svg width="14" height="11" viewBox="0 0 14 11"><rect x=".5" y=".5" width="13" height="10" rx="1" fill="none" stroke="#333"/><path d="M.5 .5 7 6l6.5-5.5" fill="none" stroke="#333"/></svg>Email Address</div>
  <div class="btn" style="left:587px;top:407px;width:119px;height:43px">Signup</div>

  <div class="footer-brand"><span class="brand-dot"></span><span class="brand-name">Brisbeck Current Glide</span></div>

  <div class="copyright-bar">
    <p>Copyright © 2022 BRISBECK CURRENT GLIDE. All Rights Reserved.</p>
    <span class="social" style="left:928px"></span>
    <span class="social" style="left:968px"></span>
    <span class="social" style="left:1008px"></span>
  </div>
</footer>

</body>
</html>
```